Bref créative
Lemon Badger
Cakes and Desserts
Bright & Fun-filled
Marla Tevison
Owner
2193 Brennick Ct.
Arvada, CO 80005
marla.tevison@postvale.net
Join us on Facebook!
I also need stationery that ties in with my business card.
Logo for cake company

```html
<!DOCTYPE html>
<html lang="en">
<head>
<meta charset="utf-8">
<title>Lemon Badger Business Cards</title>
<link rel="stylesheet" href="https://fonts.googleapis.com/css2?family=PT+Sans:wght@400;700&family=Marcellus+SC&display=swap">
<style>
  :root {
    --backdrop: #e4c79d;
    --brown: #8b4a2b;
    --pink: #e2499b;
    --white: #ffffff;
    --label: #3a2a1c;
  }
  * { margin: 0; padding: 0; box-sizing: border-box; }
  html, body { width: 1200px; height: 794px; overflow: hidden; }
  body {
    background: var(--backdrop);
    font-family: "PT Sans", Arial, sans-serif;
    position: relative;
  }
  .card {
    position: absolute;
    width: 528px;
    height: 320px;
    overflow: hidden;
    box-shadow: 0 3px 8px rgba(0,0,0,0.25);
  }
  .front-a { left: 36px; top: 36px; background: var(--white); }
  .front-b { left: 636px; top: 36px; background: var(--brown); }
  .back-a  { left: 36px; top: 398px; background: var(--white); }
  .back-b  { left: 636px; top: 398px; background: var(--brown); }

  .panel { position: absolute; top: 0; right: 0; width: 200px; height: 100%; }
  .front-a .panel { background: var(--brown); }
  .front-b .panel { background: var(--pink); }

  .brand {
    position: absolute;
    display: flex;
    align-items: center;
    gap: 14px;
    font-weight: 700;
    font-size: 34px;
    line-height: 1;
    color: var(--brown);
  }
  .brand-dot { width: 40px; height: 40px; border-radius: 50%; background: var(--pink); flex: none; }
  .front .brand { left: 26px; top: 48px; }
  .back .brand { left: 50%; top: 112px; transform: translateX(-50%); white-space: nowrap; }
  .front-b .brand, .back-b .brand { color: var(--white); }

  .holder {
    position: absolute;
    left: 26px;
    top: 256px;
    font-weight: 700;
    font-size: 17px;
    color: var(--brown);
  }
  .front-b .holder { color: var(--white); }

  .contact {
    position: absolute;
    left: 14px;
    top: 238px;
    list-style: none;
    font-size: 12px;
    line-height: 17px;
    color: var(--white);
    white-space: nowrap;
  }
  .contact b { font-weight: 700; }

  .site {
    position: absolute;
    left: 0; right: 0;
    bottom: 26px;
    text-align: center;
    font-size: 13px;
    color: var(--brown);
  }
  .back-b .site { color: var(--white); }

  .label {
    position: absolute;
    width: 528px;
    text-align: center;
    font-family: "Marcellus SC", Georgia, serif;
    font-size: 22px;
    letter-spacing: 2px;
    color: var(--label);
  }
  .label-front-a { left: 36px; top: 364px; }
  .label-front-b { left: 636px; top: 364px; }
  .label-back-a  { left: 36px; top: 736px; }
  .label-back-b  { left: 636px; top: 736px; }
</style>
</head>
<body>

<section class="card front front-a">
  <div class="brand"><span class="brand-dot"></span>Lemon Badger</div>
  <p class="holder">Marla Tevison</p>
  <div class="panel">
    <ul class="contact">
      <li><b>P:</b> (720) 555-0142</li>
      <li><b>E:</b> marla.tevison@postvale.net</li>
      <li><b>W:</b> www.lemonbadgercakes.com</li>
    </ul>
  </div>
</section>

<section class="card front front-b">
  <div class="brand"><span class="brand-dot"></span>Lemon Badger</div>
  <p class="holder">Marla Tevison</p>
  <div class="panel">
    <ul class="contact">
      <li><b>P:</b> (720) 555-0142</li>
      <li><b>E:</b> marla.tevison@postvale.net</li>
      <li><b>W:</b> www.lemonbadgercakes.com</li>
    </ul>
  </div>
</section>

<section class="card back back-a">
  <div class="brand"><span class="brand-dot"></span>Lemon Badger</div>
  <p class="site">www.lemonbadgercakes.com</p>
</section>

<section class="card back back-b">
  <div class="brand"><span class="brand-dot"></span>Lemon Badger</div>
  <p class="site">www.lemonbadgercakes.com</p>
</section>

<p class="label label-front-a">Business Card Front A</p>
<p class="label label-front-b">Business Card Front B</p>
<p class="label label-back-a">Business Card Back A</p>
<p class="label label-back-b">Business Card Back B</p>

</body>
</html>
```